BrightLoop - IT services company
Refresh Stationary
Project: BrightLoop - IT services company
BrightLoop  - IT services company -
Creative Brief
Simple
Delia Okonjo
Marketing Manager
2418 Fenwick Lane Suite 140 Durham, NC 27705
delia.okonjo@brightloop-example.com
www.brightloop-example.com

```html
<!DOCTYPE html>
<html lang="en">
<head>
<meta charset="utf-8">
<title>BrightLoop Stationery</title>
<link rel="stylesheet" href="https://fonts.googleapis.com/css2?family=Montserrat:wght@400;600;800&display=swap">
<style>
  :root{
    --bg:#e8e6e2;
    --paper:#ffffff;
    --orange:#f07d1a;
    --orange-light:#f9a646;
    --navy:#26368c;
    --navy-deep:#1c2a73;
    --ink:#3b3f52;
    --muted:#8a8fa3;
  }
  *{box-sizing:border-box;margin:0;padding:0}
  html,body{width:1200px;height:794px;overflow:hidden}
  body{background:var(--bg);font-family:"Montserrat",Arial,sans-serif;color:var(--ink);position:relative}
  .piece{position:absolute;background:var(--paper);overflow:hidden;box-shadow:0 2px 6px rgba(0,0,0,.18)}
  .piece svg.art{position:absolute;inset:0;width:100%;height:100%}
  .brand{position:absolute;display:flex;flex-direction:column;align-items:flex-start}
  .brand-row{display:flex;align-items:center;gap:6px}
  .brand-dot{border-radius:50%;background:var(--orange);flex:none}
  .brand-name{font-weight:800;color:var(--navy);line-height:1;letter-spacing:.01em;white-space:nowrap}
  .brand-tag{font-weight:600;color:var(--navy);letter-spacing:.04em;margin-top:3px;white-space:nowrap}
  .contact{position:absolute;color:#fff;font-size:7px;line-height:1.55;white-space:nowrap}
  .small-print{position:absolute;font-size:5.5px;line-height:1.5;color:var(--muted);white-space:nowrap}

  .folder-front{left:48px;top:24px;width:240px;height:360px}
  .folder-spread{left:336px;top:24px;width:528px;height:372px}
  .letterhead{left:893px;top:29px;width:254px;height:356px}
  .folder-back{left:60px;top:408px;width:252px;height:360px}
  .pocket{left:348px;top:408px;width:516px;height:348px}
  .card-front{left:893px;top:412px;width:170px;height:96px}
  .card-blue{left:910px;top:538px;width:160px;height:92px;background:linear-gradient(135deg,var(--navy) 0%,var(--navy-deep) 100%)}
  .card-orange{left:910px;top:650px;width:160px;height:92px;background:linear-gradient(135deg,var(--orange-light),var(--orange))}
</style>
</head>
<body>

<!-- Folder front cover -->
<div class="piece folder-front">
  <svg class="art" viewBox="0 0 240 360" preserveAspectRatio="none">
    <defs>
      <linearGradient id="orangeFill" x1="0" y1="0" x2="1" y2="1">
        <stop offset="0" stop-color="#f9a646"/><stop offset="1" stop-color="#ee7a16"/>
      </linearGradient>
    </defs>
    <path d="M0 0H240V18C170 46 90 20 0 44Z" fill="url(#orangeFill)"/>
    <path d="M0 44C90 20 170 46 240 18" stroke="#26368c" stroke-width="3" fill="none"/>
    <path d="M0 250C70 210 160 205 240 235V360H0Z" fill="url(#orangeFill)"/>
    <path d="M0 242C70 202 160 198 240 228" stroke="#26368c" stroke-width="4" fill="none"/>
  </svg>
  <div class="brand" style="left:36px;top:112px">
    <div class="brand-row"><span class="brand-dot" style="width:16px;height:16px"></span><span class="brand-name" style="font-size:27px">BrightLoop</span></div>
    <span class="brand-tag" style="font-size:8.5px">MANAGED IT SERVICES</span>
  </div>
</div>

<!-- Folder open spread -->
<div class="piece folder-spread">
  <svg class="art" viewBox="0 0 528 372" preserveAspectRatio="none">
    <defs>
      <linearGradient id="spreadOrange" x1="0" y1="0" x2="1" y2="1">
        <stop offset="0" stop-color="#f9a646"/><stop offset="1" stop-color="#ee7a16"/>
      </linearGradient>
      <linearGradient id="spreadNavy" x1="0" y1="0" x2="1" y2="1">
        <stop offset="0" stop-color="#2e40a0"/><stop offset="1" stop-color="#1c2a73"/>
      </linearGradient>
    </defs>
    <path d="M0 0H528V26C420 56 320 20 264 40C190 66 90 20 0 48Z" fill="url(#spreadOrange)"/>
    <path d="M0 52C90 24 190 70 264 44C320 24 420 60 528 30" stroke="#26368c" stroke-width="4" fill="none"/>
    <path d="M0 200C90 250 180 240 264 218V372H0Z" fill="url(#spreadNavy)"/>
    <path d="M264 218C330 200 420 210 528 250V372H264Z" fill="url(#spreadOrange)"/>
    <path d="M0 194C90 244 180 234 264 212C330 194 420 204 528 244" stroke="#f07d1a" stroke-width="3" fill="none"/>
    <line x1="264" y1="0" x2="264" y2="372" stroke="#d8d8de" stroke-width="1"/>
  </svg>
  <div class="brand" style="left:50px;top:98px">
    <div class="brand-row"><span class="brand-dot" style="width:9px;height:9px"></span><span class="brand-name" style="font-size:14px">BrightLoop</span></div>
    <span class="brand-tag" style="font-size:5px">MANAGED IT SERVICES</span>
  </div>
  <div class="brand" style="left:300px;top:102px">
    <div class="brand-row"><span class="brand-dot" style="width:18px;height:18px"></span><span class="brand-name" style="font-size:30px">BrightLoop</span></div>
    <span class="brand-tag" style="font-size:9.5px">MANAGED IT SERVICES</span>
  </div>
  <div class="contact" style="left:60px;top:286px">
    2418 Fenwick Lane Suite 140<br>Harlow Springs, CO 80999<br>Phone: (555) 010-0142<br>Fax: (555) 010-0187<br>delia.okonjo@brightloop-example.com<br>www.brightloop-example.com
  </div>
</div>

<!-- Letterhead -->
<div class="piece letterhead">
  <svg class="art" viewBox="0 0 254 356" preserveAspectRatio="none">
    <defs>
      <linearGradient id="lhOrange" x1="0" y1="0" x2="1" y2="0">
        <stop offset="0" stop-color="#f9a646"/><stop offset="1" stop-color="#ee7a16"/>
      </linearGradient>
    </defs>
    <path d="M0 0H254V34C190 20 120 8 0 22Z" fill="url(#lhOrange)"/>
    <path d="M0 26C120 12 190 24 254 40" stroke="#26368c" stroke-width="3" fill="none"/>
    <line x1="14" y1="338" x2="240" y2="338" stroke="#26368c" stroke-width="1"/>
  </svg>
  <div class="brand" style="left:150px;top:40px">
    <div class="brand-row"><span class="brand-dot" style="width:8px;height:8px"></span><span class="brand-name" style="font-size:14px">BrightLoop</span></div>
    <span class="brand-tag" style="font-size:4.8px">MANAGED IT SERVICES</span>
  </div>
  <div class="small-print" style="left:14px;top:322px;width:226px;text-align:center">2418 Fenwick Lane Suite 140, Harlow Springs, CO 80999</div>
  <div class="small-print" style="left:14px;top:341px;width:226px;text-align:center">Tel (555) 010-0142 · www.brightloop-example.com</div>
</div>

<!-- Folder back cover -->
<div class="piece folder-back">
  <svg class="art" viewBox="0 0 252 360" preserveAspectRatio="none">
    <defs>
      <linearGradient id="backOrange" x1="0" y1="0" x2="1" y2="1">
        <stop offset="0" stop-color="#f9a646"/><stop offset="1" stop-color="#ee7a16"/>
      </linearGradient>
      <linearGradient id="backNavy" x1="0" y1="0" x2="1" y2="1">
        <stop offset="0" stop-color="#2e40a0"/><stop offset="1" stop-color="#1c2a73"/>
      </linearGradient>
    </defs>
    <path d="M0 0H252V40C170 20 80 24 0 44Z" fill="url(#backOrange)"/>
    <path d="M0 48C80 28 170 24 252 44" stroke="#26368c" stroke-width="3" fill="none"/>
    <path d="M0 190C90 176 200 200 252 250V360H0Z" fill="url(#backNavy)"/>
    <path d="M0 184C90 170 200 194 252 244" stroke="#f07d1a" stroke-width="3" fill="none"/>
  </svg>
  <div class="brand" style="left:60px;top:120px">
    <div class="brand-row"><span class="brand-dot" style="width:10px;height:10px"></span><span class="brand-name" style="font-size:17px">BrightLoop</span></div>
    <span class="brand-tag" style="font-size:5.8px">MANAGED IT SERVICES</span>
  </div>
  <div class="contact" style="left:66px;top:268px">2418 Fenwick Lane Suite 140<br>Harlow Springs, CO 80999</div>
</div>

<!-- Pocket inside -->
<div class="piece pocket">
  <svg class="art" viewBox="0 0 516 348" preserveAspectRatio="none">
    <defs>
      <linearGradient id="pocketOrange" x1="0" y1="0" x2="1" y2="0">
        <stop offset="0" stop-color="#ee7a16"/><stop offset="1" stop-color="#f9a646"/>
      </linearGradient>
    </defs>
    <circle cx="110" cy="92" r="54" fill="#eef0f6"/>
    <line x1="258" y1="0" x2="258" y2="348" stroke="#dcdce2" stroke-width="1"/>
    <path d="M0 296H230L258 270V348H0Z" fill="url(#pocketOrange)"/>
    <path d="M0 270H258" stroke="#dcdce2" stroke-width="1" fill="none"/>
    <path d="M258 270H516V348H258Z" fill="#fafafa"/>
    <path d="M258 270L286 298H516V348H258Z" fill="url(#pocketOrange)"/>
    <path d="M300 276L316 262H350L366 276" stroke="#c9ccd6" stroke-width="1" fill="none"/>
  </svg>
  <div class="brand" style="left:18px;top:302px">
    <div class="brand-row"><span class="brand-dot" style="width:8px;height:8px;background:#fff"></span><span class="brand-name" style="font-size:14px">BrightLoop</span></div>
    <span class="brand-tag" style="font-size:4.8px;color:#fff">MANAGED IT SERVICES</span>
  </div>
</div>

<!-- Business card front -->
<div class="piece card-front">
  <svg class="art" viewBox="0 0 170 96" preserveAspectRatio="none">
    <path d="M0 0H170V12C110 26 60 4 0 18Z" fill="#f28a26"/>
    <path d="M0 21C60 7 110 29 170 15" stroke="#26368c" stroke-width="2" fill="none"/>
  </svg>
  <div class="brand" style="left:8px;top:30px">
    <div class="brand-row"><span class="brand-dot" style="width:6px;height:6px"></span><span class="brand-name" style="font-size:10px">BrightLoop</span></div>
    <span class="brand-tag" style="font-size:3.6px">MANAGED IT SERVICES</span>
  </div>
  <div style="position:absolute;left:86px;top:30px;font-size:6px;line-height:1.4;color:var(--navy);white-space:nowrap">
    <strong style="font-weight:800">Delia Okonjo</strong><br><span style="color:var(--muted)">Marketing Manager</span>
  </div>
  <div class="small-print" style="left:86px;top:56px;font-size:3.8px">2418 Fenwick Lane Suite 140<br>Harlow Springs, CO 80999<br>(555) 010-0142<br>delia.okonjo@brightloop-example.com</div>
</div>

<!-- Business card back, blue -->
<div class="piece card-blue"></div>

<!-- Business card back, orange -->
<div class="piece card-orange"></div>

</body>
</html>
```